Velborne Systems needs a business card

The logo we have uploaded is going to be the image centered on the back.
The business card color is going to be black. Increase the contrast in the logo and lettering so the grey stands out from the black and is more readable. Keep the shadow effect if you can.
On the front, the only part of the logo that should be used is the Egyptian character. We would like the following information included: Name (first last), Title, Phone number, email and company name (Velborne Systems).
The images of colored sound waves we uploaded is a concept we would like implemented on the front as well but please do not use the exact image. It is for guideline purposes.
Get creative with the empty space. We are a technology company that deals with sound and lights. Please not too busy.
Thank you, we look forward to all your submissions.

```html
<!DOCTYPE html>
<html lang="en">
<head>
<meta charset="utf-8">
<title>Velborne Systems – Business Card Front</title>
<link href="https://fonts.googleapis.com/css2?family=Exo+2:wght@400;600&display=swap" rel="stylesheet">
<style>
  :root{
    --stage:#e6e4e1;
    --card-dark:#1f2022;
    --card-red:#ee3b3b;
    --swoosh:#8d8e90;
    --logo-grey:#d9d9db;
    --wave-grey:#5a5b5e;
    --accent-red:#ee3b3b;
    --ink-light:#ffffff;
  }
  *{box-sizing:border-box;margin:0;padding:0}
  html,body{width:1200px;height:899px;overflow:hidden}
  body{background:var(--stage);font-family:"Exo 2",sans-serif;position:relative}
  .card{
    position:absolute;left:110px;top:170px;width:980px;height:560px;
    border-radius:34px;overflow:hidden;background:var(--card-dark);
    box-shadow:0 10px 30px rgba(0,0,0,.18);
  }
  .card-bg{position:absolute;inset:0;width:100%;height:100%}
  .brand{
    position:absolute;left:80px;top:190px;display:flex;align-items:center;gap:20px;
  }
  .brand-mark{width:40px;height:40px;background:var(--accent-red);flex:none}
  .brand-name{
    font-weight:600;font-size:36px;letter-spacing:3px;text-transform:uppercase;
    color:var(--logo-grey);line-height:1.1;
    text-shadow:0 2px 4px rgba(0,0,0,.6);
  }
  .contact{position:absolute;left:690px;top:62px;color:var(--ink-light)}
  .person-name{font-weight:600;font-size:24px;letter-spacing:1.5px;text-transform:uppercase}
  .person-title{font-weight:400;font-size:19px;letter-spacing:1px;margin-top:4px}
  .address{position:absolute;left:690px;top:200px;color:var(--ink-light);font-size:20px;line-height:1.35}
  .details{position:absolute;left:640px;top:352px;list-style:none;color:var(--ink-light);font-size:17px;letter-spacing:1px}
  .details li{display:flex;align-items:center;gap:14px;height:32px}
  .details svg{width:16px;height:16px;flex:none}
</style>
</head>
<body>
  <section class="card" aria-label="Velborne Systems business card front">
    <svg class="card-bg" viewBox="0 0 980 560" preserveAspectRatio="none" aria-hidden="true">
      <path d="M640 0 C610 260 520 460 330 560 L290 560 C480 450 570 250 590 0 Z" fill="var(--swoosh)"/>
      <path d="M640 0 C610 260 520 460 330 560 L980 560 L980 0 Z" fill="var(--card-red)"/>
      <g class="sound-bars" fill="var(--wave-grey)">
        <rect x="80" y="478" width="6" height="14" rx="3"/>
        <rect x="96" y="468" width="6" height="34" rx="3"/>
        <rect x="112" y="456" width="6" height="58" rx="3"/>
        <rect x="128" y="470" width="6" height="30" rx="3"/>
        <rect x="144" y="448" width="6" height="74" rx="3"/>
        <rect x="160" y="462" width="6" height="46" rx="3"/>
        <rect x="176" y="474" width="6" height="22" rx="3"/>
        <rect x="192" y="458" width="6" height="54" rx="3"/>
        <rect x="208" y="470" width="6" height="30" rx="3"/>
        <rect x="224" y="480" width="6" height="10" rx="3"/>
        <rect x="240" y="472" width="6" height="26" rx="3"/>
        <rect x="256" y="480" width="6" height="10" rx="3"/>
      </g>
      <rect x="80" y="483" width="260" height="4" rx="2" fill="var(--accent-red)" opacity=".8"/>
    </svg>

    <div class="brand">
      <span class="brand-mark"></span>
      <span class="brand-name">Velborne<br>Systems</span>
    </div>

    <div class="contact">
      <p class="person-name">Marcus Dellow</p>
      <p class="person-title">Managing Director</p>
    </div>

    <p class="address">047,12th floor,Arden Quay<br>Road KLN</p>

    <ul class="details">
      <li><svg viewBox="0 0 16 16" fill="#fff"><path d="M3 1l3 3-1.5 2a9 9 0 0 0 5.5 5.5L12 10l3 3-2 2C7 15 1 9 1 3z"/></svg>014 555 0192</li>
      <li><svg viewBox="0 0 16 16" fill="none" stroke="#fff" stroke-width="1.8"><rect x="4" y="1" width="8" height="14" rx="1.5"/><circle cx="8" cy="12" r=".6" fill="#fff"/></svg>014 555 0193</li>
      <li><svg viewBox="0 0 16 16" fill="#fff"><rect x="1" y="6" width="14" height="8" rx="1"/><rect x="4" y="1" width="8" height="5"/></svg>014 555 0194</li>
      <li><svg viewBox="0 0 16 16" fill="none" stroke="#fff" stroke-width="1.6"><rect x="1" y="3" width="14" height="10" rx="1"/><path d="M1 4l7 5 7-5"/></svg>hello@velborne.com</li>
      <li><svg viewBox="0 0 16 16" fill="none" stroke="#fff" stroke-width="1.4"><circle cx="8" cy="8" r="7"/><ellipse cx="8" cy="8" rx="3" ry="7"/><path d="M1 8h14"/></svg>www.velbornesystems.com</li>
    </ul>
  </section>
</body>
</html>
```